Information Technology Company needs a Website...

We need a single page website for new technology company called:

MERIDEL FALLS TECHNOLOGY GROUP
Based in Ojai CA.

We are offering three primary services:

- Business Solutions

- IT Services

- Software Implementation and Consulting

We want a single page design where all content scrolls down/up on one page. We're looking for the following characteristics:

- Home/Landing
- Active background with panoramic view (Will provide content)

- Business Solutions, IT Services, Software Implementation and Consulting

List of software vendors we recommend (Company logos)

- About
- History
- Our Team
- Partners

I'll upload our new logo as soon as we get the design files. I'll also send over some example website layout's that we like shortly.

Target Market(s)

Small/Medium Businesses

Industry/Entity Type

Information Technology

Number of Pages Required

1 page

Font styles to use
Other font styles liked:
• Sansation

Requirements
Must have
• Full page browser width, easy navigation and visibility. Creative design, not like every other "Technology" website template. Should be the "One Page" design where each section is below the next and the user scrolls down the page through the whole site. I like the concept of the following website in the main "Whiteboard" image:
• http://www.plavorix.com/design/4829137
• And the way this site does the active panoramic background:
• http://www.kelbrantworks.com/
• Something interesting and appealing to potential clients looking for Small/Medium business solutions and IT Services.
• Use uploaded Logo to establish color and theme for website.
Should not have
• Look the same as every other information technology website template.

```html
<!DOCTYPE html>
<html lang="en">
<head>
<meta charset="utf-8">
<title>Meridel Falls Technology Group</title>
<link rel="stylesheet" href="https://fonts.googleapis.com/css2?family=Open+Sans:ital,wght@0,400;0,600;0,700;0,800;1,700&display=swap">
<style>
:root{
  --orange:#f15a24;
  --orange-light:#ff8a55;
  --orange-deep:#f04e1a;
  --ink:#333;
  --grey-text:#777;
  --panel:#e6e6e6;
  --card:#c8c8c8;
  --card-foot:#a9a9a9;
  --dark:#2b2b2b;
  --footer:#141414;
  --green:#8cc63f;
  --partner-grey:#8a8a8a;
  --partner-blue:#3fb7e8;
  --white:#fff;
}
*{box-sizing:border-box;margin:0;padding:0}
html,body{width:1200px;height:3279px;overflow:hidden}
body{position:relative;font-family:"Open Sans",Arial,sans-serif;color:var(--ink);background:var(--white)}
.abs{position:absolute}

/* header */
.site-header{left:0;top:0;width:1200px;height:138px;background:linear-gradient(#fff,#f0f0f0)}
.brand{left:164px;top:36px;color:#3a3a3a;font-weight:700;line-height:1}
.brand-name{font-size:34px;letter-spacing:-.5px}
.brand-sub{font-size:13px;letter-spacing:2.6px;margin-top:6px}
.enquiry{left:818px;top:36px;font-size:18px;color:#555}
.enquiry span{color:var(--orange);margin-left:14px}
.main-nav{left:457px;top:80px;font-size:16px}
.main-nav a{position:absolute;white-space:nowrap;text-decoration:none;color:#9a9a9a}
.main-nav a.active{color:var(--orange)}
.nav-bar{left:456px;top:130px;width:46px;height:8px;background:var(--orange)}

/* hero */
.hero{left:0;top:138px;width:1200px;height:605px;
  background:linear-gradient(#4f5673 0%,#8d7694 18%,#d597a6 36%,#f0ae9e 48%,#c98f98 56%,#6f6675 66%,#3d3c47 82%,#25242b 100%)}
.hero-title{left:153px;top:245px;font-size:60px;line-height:62px;color:var(--white);font-weight:400}
.hero-note{left:874px;top:462px;font-size:22px;color:var(--white)}
.pill{left:484px;top:717px;width:248px;height:46px;border:3px solid var(--white);border-radius:14px;
  background:var(--orange);color:var(--white);font-weight:700;font-size:24px;text-align:center;line-height:40px;letter-spacing:1px}

/* about */
.about-text{left:140px;top:795px;width:920px;font-size:20px;line-height:30px;text-align:center;color:#222}
.know-more{left:966px;top:913px;font-size:11px;color:#333;display:flex;align-items:center;gap:8px}
.ring-arrow{width:32px;height:32px;border:2px solid var(--orange);border-radius:50%;display:flex;align-items:center;justify-content:center}

/* services */
.services{left:0;top:962px;width:1200px;height:538px;background:linear-gradient(#ff9468,var(--orange-deep))}
.section-title{width:1200px;left:0;text-align:center;font-weight:800;font-size:24px}
.services .section-title{top:22px;color:var(--white)}
.service{width:280px;height:280px;border:4px solid var(--white);border-radius:50%;
  background:radial-gradient(circle at 50% 35%,#ff8d5a,#f2561f);color:var(--white);text-align:center;padding-top:40px}
.service h3{font-size:15px;font-weight:700;margin-top:12px;line-height:17px}
.service p{font-size:11px;line-height:16px;width:170px;margin:10px auto 0}
.view-more{width:78px;height:78px;border:3px solid var(--white);border-radius:50%;background:#f7804f;
  color:var(--white);font-size:10px;font-weight:700;text-align:center;line-height:72px}

/* team */
.team{left:0;top:1500px;width:1200px;height:507px;background:var(--panel)}
.title-rule{display:flex;align-items:center;justify-content:center;gap:14px;color:#333}
.title-rule i{display:block;width:60px;height:2px;background:var(--orange);position:relative}
.title-rule i::before{content:"";position:absolute;top:-4px;width:10px;height:10px;border-radius:50%;background:var(--orange)}
.title-rule i.l::before{left:0}.title-rule i.r::before{right:0}
.card{top:87px;width:210px;height:319px;background:var(--card);border-radius:8px;text-align:center;overflow:hidden}
.card.active{background:#eaeaea;border:2px solid #bdbdbd}
.avatar{width:128px;height:128px;border-radius:50%;margin:16px auto 0;border:3px solid #fff;
  background:radial-gradient(circle at 50% 40%,#c98a6a,#7b3a2a 70%,#e05b3a)}
.avatar.alt{background:radial-gradient(circle at 50% 40%,#e0b08f,#8a5a38 70%,#5a3c28)}
.card h4{color:var(--orange);font-size:19px;font-weight:700;margin-top:10px;line-height:20px}
.card .role{font-size:12px;color:#333;line-height:14px}
.card p{font-size:10px;font-weight:700;line-height:13px;color:#333;width:160px;margin:8px auto 0}
.card-foot{position:absolute;left:0;bottom:0;width:100%;height:30px;background:var(--card-foot);
  display:flex;align-items:center;justify-content:center;gap:8px}
.card.active .card-foot{background:var(--orange)}
.dot{width:12px;height:12px;border-radius:50%;background:#fff}
.slider-arrow{top:203px;width:70px;height:70px;border:3px solid #fff;border-radius:50%;display:flex;align-items:center;justify-content:center}
.pager{left:556px;top:455px;display:flex;gap:10px}
.pager span{width:16px;height:16px;border-radius:50%;background:#bdbdbd}
.pager span.on{background:var(--orange)}

/* news */
.news{left:0;top:2007px;width:1200px;height:573px;background:radial-gradient(ellipse at 60% 50%,#555,#2e2e2e 70%,#262626)}
.news-title{left:138px;top:36px;font-size:24px;font-weight:700;color:#fff}
.news-title b{color:var(--orange)}
.more-news{left:525px;top:40px;font-size:11px;color:#fff;display:flex;align-items:center;gap:8px}
.more-news .ring-arrow{border-color:#fff}
.news-item{left:125px;width:428px;height:125px;background:rgba(25,25,25,.78)}
.thumb{position:absolute;left:15px;top:15px;width:96px;height:96px;background:linear-gradient(#a8c3d8,#c9b79a 55%,#5d7a3d)}
.news-item h5{position:absolute;left:133px;top:10px;font-size:16px;color:#fff;font-weight:700}
.news-item .date{position:absolute;left:133px;top:31px;font-size:11px;color:#aaa}
.news-item .date b{color:var(--orange);font-weight:600}
.news-item p{position:absolute;left:133px;top:47px;width:250px;font-size:13.5px;line-height:17px;color:#fff}
.news-item .read{position:absolute;right:48px;bottom:6px;font-size:9px;color:#ccc}
.timeline{left:615px;top:2018px;width:2px;height:534px;background:var(--orange)}
.t-dot{width:10px;height:10px;border-radius:50%;background:var(--orange)}
.t-link{height:2px;background:var(--orange);width:62px;left:553px}
.bubble{left:834px;top:2066px}
.bubble-text{left:834px;top:2106px;width:212px;text-align:center;font-style:italic;font-weight:700;font-size:27px;line-height:32px;color:#fff}
.bubble-text b{color:var(--orange)}
.quote{left:667px;top:2326px;width:390px;height:188px;background:rgba(40,40,40,.85)}
.quote p{position:absolute;left:72px;top:15px;width:260px;font-size:14px;line-height:17px;color:#fff}
.quote .mark{position:absolute;font-size:30px;color:var(--orange);font-weight:800;font-style:italic;line-height:1}
.q-photo{position:absolute;left:50px;top:78px;width:95px;height:95px;background:linear-gradient(#d9b49a,#8d5e40)}
.quote h6{position:absolute;left:165px;top:108px;font-size:15px;color:var(--orange);font-weight:700}
.quote .role{position:absolute;left:165px;top:132px;font-size:11px;font-style:italic;color:#ddd}
.next{left:1078px;top:2388px;font-size:10px;color:#fff;text-align:center}
.next .ring-arrow{border-color:#fff;margin-top:2px}

/* partners */
.partners{left:0;top:2580px;width:1200px;height:251px;background:#ececec}
.partner{top:148px;font-size:30px;font-weight:700;color:var(--partner-grey);white-space:nowrap;display:flex;align-items:center}
.partner.small{top:154px;font-size:20px}
.partner.blue{color:var(--partner-blue)}
.p-circle{left:143px;top:140px;width:62px;height:62px;border-radius:50%;background:#9a9a9a}

/* footer */
.site-footer{left:0;top:2831px;width:1200px;height:387px;background:var(--footer);color:#fff}
.f-col{top:80px;font-size:14px;line-height:24px}
.f-col h6{font-size:15px;color:var(--orange);font-weight:700;letter-spacing:.3px;margin-bottom:20px}
.f-row{display:flex;align-items:center;gap:18px;margin-bottom:22px}
.news-input{width:213px;height:24px;background:#bbb;border-radius:2px;font-size:12px;color:#666;padding-left:32px;line-height:24px;margin-top:10px}
.subscribe{width:96px;height:26px;background:var(--green);border-radius:3px;color:#234;font-size:14px;text-align:center;line-height:26px;margin:12px 0 0 117px}
.bottom-bar{left:0;top:3218px;width:1200px;height:61px;background:var(--orange);color:#fff;font-size:11px;text-align:center;padding-top:16px;line-height:14px}
</style>
</head>
<body>

<header class="site-header abs">
  <div class="brand abs"><div class="brand-name">Meridel Falls</div><div class="brand-sub">TECHNOLOGY GROUP</div></div>
  <div class="enquiry abs">Make an Enquiry<span>+0123 456 789</span></div>
  <nav class="main-nav abs">
    <a class="active" style="left:0">Home</a>
    <a style="left:78px">About</a>
    <a style="left:157px">History</a>
    <a style="left:243px">Our Team</a>
    <a style="left:350px">Partners</a>
    <a style="left:444px">Services</a>
    <a style="left:540px">Contact Us</a>
  </nav>
  <div class="nav-bar abs"></div>
</header>

<section class="hero abs" role="img" aria-label="Panoramic photo of a lake at sunset with pink sky and rocky shore">
  <h1 class="hero-title abs">Your Text<br>Goes Here</h1>
  <div class="hero-note abs">Panoramic image goes here</div>
</section>
<div class="pill abs">WHO WE ARE</div>

<p class="about-text abs">Lorem Ipsum is simply dummy text of the printing and typesetting industry. Lorem Ipsum has been the industry's standard dummy text ever since the 1500s, when an unknown printer took a galley of type and scrambled it to make a type specimen book. It has survived not only five centuries, but also the leap into electronic typesetting, remaining essentially unchanged.</p>
<div class="know-more abs">Know More <span class="ring-arrow"><svg width="10" height="14"><path d="M2 1l6 6-6 6" stroke="#f15a24" stroke-width="2" fill="none"/></svg></span></div>

<section class="services abs">
  <h2 class="section-title abs">OUR SERVICES</h2>
  <div class="service abs" style="left:138px;top:116px">
    <svg width="64" height="56" viewBox="0 0 64 56"><rect x="6" y="8" width="44" height="30" rx="2" fill="none" stroke="#fff" stroke-width="4"/><rect x="22" y="40" width="12" height="6" fill="#fff"/><rect x="14" y="46" width="28" height="4" fill="#fff"/><circle cx="52" cy="12" r="8" fill="none" stroke="#fff" stroke-width="4"/><rect x="50" y="20" width="4" height="30" fill="#fff"/></svg>
    <h3>IT Services</h3>
    <p>Lorem Ipsum is simply dummy text of the printing and typesetting industry. Lorem</p>
  </div>
  <div class="view-more abs" style="left:348px;top:356px">View More</div>
  <div class="service abs" style="left:459px;top:116px">
    <svg width="70" height="56" viewBox="0 0 70 56"><path d="M4 22l14-12 12 6 10-4 26 12-10 8" fill="none" stroke="#fff" stroke-width="5" stroke-linejoin="round"/><path d="M16 30l18 16 20-14" fill="none" stroke="#fff" stroke-width="5" stroke-linecap="round"/></svg>
    <h3>Business Solutions</h3>
    <p>Lorem Ipsum is simply dummy text of the printing and typesetting industry. Lorem</p>
  </div>
  <div class="view-more abs" style="left:669px;top:356px">View More</div>
  <div class="service abs" style="left:780px;top:116px">
    <svg width="60" height="60" viewBox="0 0 60 60"><circle cx="30" cy="30" r="20" fill="none" stroke="#fff" stroke-width="6" stroke-dasharray="8 5"/><circle cx="30" cy="30" r="10" fill="none" stroke="#fff" stroke-width="4"/></svg>
    <h3>Software Implementation<br>&amp; Consulting</h3>
    <p>Lorem Ipsum is simply dummy text of the printing and typesetting industry. Lorem</p>
  </div>
  <div class="view-more abs" style="left:990px;top:356px">View More</div>
</section>

<section class="team abs">
  <h2 class="section-title title-rule abs" style="top:20px"><i class="l"></i>MEET OUR TEAM<i class="r"></i></h2>
  <div class="slider-arrow abs" style="left:40px"><svg width="16" height="26"><path d="M13 2L3 13l10 11" stroke="#fff" stroke-width="3" fill="none"/></svg></div>
  <div class="slider-arrow abs" style="left:1087px"><svg width="16" height="26"><path d="M3 2l10 11-10 11" stroke="#fff" stroke-width="3" fill="none"/></svg></div>

  <div class="card active abs" style="left:131px">
    <div class="avatar" role="img" aria-label="Team member portrait"></div>
    <h4>Name Here</h4><div class="role">Designation</div>
    <p>LoremIpsumissimply dummy text of the printing andypesettingindustry. Lorem Ipsum has been the industry'standard dummy text ever</p>
    <div class="card-foot"><svg width="16" height="16"><path d="M3 1l4 1 1 4-2 2a9 9 0 004 4l2-2 4 1v4c-8 1-15-6-15-14z" fill="#fff"/></svg><svg width="18" height="13"><rect width="18" height="13" fill="#fff"/><path d="M0 0l9 7 9-7" stroke="#f15a24" stroke-width="1.5" fill="none"/></svg><span class="dot"></span><span class="dot"></span></div>
  </div>
  <div class="card abs" style="left:374px">
    <div class="avatar alt" role="img" aria-label="Team member portrait"></div>
    <h4>Name Here</h4><div class="role">Designation</div>
    <p>LoremIpsumissimply dummy text of the printing andypesettingindustry. Lorem Ipsum has been the industry'standard dummy text ever</p>
    <div class="card-foot"><svg width="16" height="16"><path d="M3 1l4 1 1 4-2 2a9 9 0 004 4l2-2 4 1v4c-8 1-15-6-15-14z" fill="#fff"/></svg><svg width="18" height="13"><rect width="18" height="13" fill="#fff"/><path d="M0 0l9 7 9-7" stroke="#a9a9a9" stroke-width="1.5" fill="none"/></svg><span class="dot"></span><span class="dot"></span></div>
  </div>
  <div class="card abs" style="left:610px">
    <div class="avatar" role="img" aria-label="Team member portrait"></div>
    <h4>Name Here</h4><div class="role">Designation</div>
    <p>LoremIpsumissimply dummy text of the printing andypesettingindustry. Lorem Ipsum has been the industry'standard dummy text ever</p>
    <div class="card-foot"><svg width="16" height="16"><path d="M3 1l4 1 1 4-2 2a9 9 0 004 4l2-2 4 1v4c-8 1-15-6-15-14z" fill="#fff"/></svg><svg width="18" height="13"><rect width="18" height="13" fill="#fff"/><path d="M0 0l9 7 9-7" stroke="#a9a9a9" stroke-width="1.5" fill="none"/></svg><span class="dot"></span><span class="dot"></span></div>
  </div>
  <div class="card abs" style="left:846px">
    <div class="avatar" role="img" aria-label="Team member portrait"></div>
    <h4>Name Here</h4><div class="role">Designation</div>
    <p>LoremIpsumissimply dummy text of the printing andypesettingindustry. Lorem Ipsum has been the industry'standard dummy text ever</p>
    <div class="card-foot"><svg width="16" height="16"><path d="M3 1l4 1 1 4-2 2a9 9 0 004 4l2-2 4 1v4c-8 1-15-6-15-14z" fill="#fff"/></svg><svg width="18" height="13"><rect width="18" height="13" fill="#fff"/><path d="M0 0l9 7 9-7" stroke="#a9a9a9" stroke-width="1.5" fill="none"/></svg><span class="dot"></span><span class="dot"></span></div>
  </div>
  <div class="pager abs"><span class="on"></span><span></span><span></span><span></span></div>
</section>

<section class="news abs">
  <h2 class="news-title abs"><b>LATEST</b> NEWS</h2>
  <div class="more-news abs">More News <span class="ring-arrow"><svg width="10" height="14"><path d="M2 1l6 6-6 6" stroke="#fff" stroke-width="2" fill="none"/></svg></span></div>
</section>
<div class="news-item abs" style="top:2127px"><div class="thumb" role="img" aria-label="Photo of a house"></div><h5>Ttitle Goes Here</h5><div class="date"><b>Emil</b> | 20/05/2016</div><p>Lorem Ipsum is simply dummy text of the printing and typesetting industry. Lorem Ipsum has been the</p><span class="read">Read More..</span></div>
<div class="news-item abs" style="top:2259px"><div class="thumb" role="img" aria-label="Photo of a house"></div><h5>Ttitle Goes Here</h5><div class="date"><b>Arlo</b> | 20/05/2016</div><p>Lorem Ipsum is simply dummy text of the printing and typesetting industry. Lorem Ipsum has been the</p><span class="read">Read More..</span></div>
<div class="news-item abs" style="top:2391px"><div class="thumb" role="img" aria-label="Photo of a house"></div><h5>Ttitle Goes Here</h5><div class="date"><b>Soren</b> | 20/05/2016</div><p>Lorem Ipsum is simply dummy text of the printing and typesetting industry. Lorem Ipsum has been the</p><span class="read">Read More..</span></div>
<div class="timeline abs"></div>
<div class="t-dot abs" style="left:611px;top:2014px"></div>
<div class="t-dot abs" style="left:611px;top:2548px"></div>
<div class="t-link abs" style="top:2253px"></div>
<div class="t-link abs" style="top:2385px"></div>

<svg class="bubble abs" width="230" height="260" viewBox="0 0 230 260" aria-hidden="true">
  <circle cx="115" cy="113" r="101" fill="#1e1e1e" stroke="#f15a24" stroke-width="9"/>
  <path d="M82 205 L72 250 L130 210" fill="#1e1e1e" stroke="#f15a24" stroke-width="9" stroke-linejoin="round"/>
  <path d="M84 196 L128 206" stroke="#1e1e1e" stroke-width="10"/>
</svg>
<div class="bubble-text abs">WHAT'S<br>PEOPLE<br><b>SAYING?</b></div>

<div class="quote abs">
  <span class="mark" style="left:50px;top:12px">"</span>
  <p>Lorem Ipsum is simply dummy text of the printing and typesetting industry. Lorem Ipsum has been the</p>
  <span class="mark" style="left:328px;top:44px">"</span>
  <div class="q-photo" role="img" aria-label="Portrait of the client giving the testimonial"></div>
  <h6>Renata Vasquez</h6>
  <div class="role">Designation</div>
</div>
<div class="next abs">Next<div class="ring-arrow"><svg width="10" height="14"><path d="M2 1l6 6-6 6" stroke="#fff" stroke-width="2" fill="none"/></svg></div></div>

<section class="partners abs">
  <h2 class="section-title title-rule abs" style="top:40px"><i class="l"></i>OUR PARTNERS<i class="r"></i></h2>
  <div class="p-circle abs"></div>
  <div class="partner abs" style="left:276px">Trelvano</div>
  <div class="partner small abs" style="left:478px">Quessim</div>
  <div class="partner small abs" style="left:632px">Vandruk</div>
  <div class="partner blue abs" style="left:812px">Zorbelle</div>
  <div class="partner abs" style="left:990px">Plixa</div>
</section>

<footer class="site-footer abs">
  <div class="f-col abs" style="left:149px">
    <h6>CONTACT US</h6>
    <div class="f-row"><svg width="16" height="22"><path d="M8 0a8 8 0 00-8 8c0 6 8 14 8 14s8-8 8-14a8 8 0 00-8-8z" fill="#f15a24"/><circle cx="8" cy="8" r="3" fill="#141414"/></svg>Your Address Goes Here</div>
    <div class="f-row"><svg width="18" height="18"><path d="M3 1l4 1 1 4-2 2a9 9 0 004 4l2-2 4 1v4c-8 1-15-6-15-14z" fill="#f15a24"/></svg>+0123 456 789</div>
    <div class="f-row"><svg width="18" height="13"><rect width="18" height="13" fill="#f15a24"/><path d="M0 0l9 7 9-7" stroke="#141414" stroke-width="1.5" fill="none"/></svg>Youremailaddressgoeshere</div>
    <div class="f-row" style="gap:8px"><span class="dot" style="width:20px;height:20px;background:#aaa"></span><span class="dot" style="width:20px;height:20px;background:#aaa"></span></div>
  </div>
  <div class="f-col abs" style="left:439px">
    <h6>CUSTOMER SERVICE</h6>
    Lorem Ipsum<br>Lorem Ipsum<br>Lorem Ipsum<br>Lorem Ipsum<br>Lorem Ipsum<br>Lorem Ipsum<br>Lorem Ipsum
  </div>
  <div class="f-col abs" style="left:675px">
    <h6>QUICK LINKS</h6>
    Faq<br>New<br>About Us<br>Privacy Policy<br>Terms of Use
  </div>
  <div class="f-col abs" style="left:862px">
    <h6 style="margin-left:23px">NEWS LETTER SIGN UP</h6>
    Subscribe to our News Letter
    <div class="news-input">E-mail</div>
    <div class="subscribe">Subscribe</div>
  </div>
</footer>
<div class="bottom-bar abs">HOME | SITE MAP | POLICIES | ARTICLES | CONTACT US | PRINT THIS PAGE | RSS rss | TOP OF PAGE<br>COPYRIGHT © 2016 Meridel Falls</div>

</body>
</html>
```